Patent Law

Need to develop a home page for a patent lawyer.

Colors should go with logo, blues...

Company Name- Velric Dunmore, PLLC

Company Overview-

I am an Intellectual Property Lawyer and focus on patents, copyrights, trademarks, & trade secrets. I work with small businesses and start ups in the chemical and biotech industries.

Why Us-

I am small firm that can provide large-firm service at a reasonable price. I also can charge flat-fees for entreprenuers in certain practice areas.

Services-
Intellectual Property
Patents
Copyrights
Trademarks
Trade secrets
Healthcare Compliance
Elder law
Wills
Trusts

Website we like-
http://www.tolvanecrest.com/ - within industry!!
http://www.quarnhollet.com/
http://brevicktallon.com/
http://thegravelwrights.com/

Target Market(s)

My customers will be small business, specifically small start-up companies in the chemical and biotech arena.

Industry/Entity Type

Trade

Requirements
Must have
• Colors should go with logo, blues...

```html
<!DOCTYPE html>
<html lang="en">
<head>
<meta charset="utf-8">
<title>Velric Dunmore, PLLC — Home</title>
<link rel="stylesheet" href="https://fonts.googleapis.com/css2?family=Montserrat:wght@400;500;600&family=Roboto+Condensed:wght@700&family=Open+Sans:wght@400&display=swap">
<style>
  :root{
    --blue:#1a6fb0;
    --blue-deep:#1450a3;
    --ink:#2b2b2b;
    --text:#555;
    --muted:#9a9a9a;
    --rule:#dedede;
    --footer:#333;
    --white:#fff;
  }
  *{box-sizing:border-box;margin:0;padding:0}
  html,body{width:1200px;height:916px;overflow:hidden;background:var(--white)}
  body{position:relative;font-family:"Montserrat",sans-serif;color:var(--text)}

  .site-header{position:absolute;left:0;top:0;width:1200px;height:114px}
  .brand{position:absolute;left:132px;top:30px;display:flex;align-items:center;gap:10px}
  .brand-mark{width:34px;height:34px;border-radius:50%;background:var(--blue-deep)}
  .brand-name{font-family:"Montserrat",sans-serif;font-weight:600;font-size:15px;color:var(--ink);letter-spacing:.3px}
  .utility{position:absolute;right:132px;top:16px;display:flex;gap:26px;font-size:13px;color:#666;align-items:center}
  .utility span{display:flex;align-items:center;gap:6px}
  .main-nav{position:absolute;right:132px;top:68px;display:flex;gap:30px}
  .main-nav a{font-size:15px;font-weight:500;color:var(--ink);text-decoration:none;letter-spacing:.6px;padding-bottom:6px}
  .main-nav a.active{color:var(--blue-deep);border-bottom:2px solid var(--blue-deep)}

  .hero{position:absolute;left:0;top:114px;width:1200px;height:402px;
    background:radial-gradient(circle at 20% 40%,#fafafa,#e6e8ea 70%,#d9dcdf)}
  .hero-photo{position:absolute;left:623px;top:0;width:577px;height:402px;
    background:linear-gradient(135deg,#6f7f5a 0%,#9aa585 30%,#c9c4bb 55%,#7c8389 100%)}
  .hero-title{position:absolute;left:132px;top:88px;font-family:"Roboto Condensed",sans-serif;font-weight:700;font-size:44px;color:var(--ink);letter-spacing:.3px}
  .hero-title em{font-style:normal;color:var(--blue-deep)}
  .hero-text{position:absolute;left:133px;top:152px;width:390px;font-family:"Open Sans",sans-serif;font-size:15.5px;line-height:21.6px;color:#444}
  .slider-dots{position:absolute;left:132px;top:360px;display:flex;gap:5px}
  .slider-dots i{width:13px;height:13px;border-radius:50%;border:1.5px solid #ccc;background:#f3f3f3}
  .slider-dots i.on{border-color:var(--blue-deep);background:radial-gradient(circle,var(--blue-deep) 45%,#fff 50%)}

  .col{position:absolute;top:566px;width:280px}
  .col h2{font-size:27px;font-weight:600;color:var(--blue);letter-spacing:.5px;margin-top:4px}
  .col-icon{position:absolute;right:0;top:0;width:41px;height:41px;border-radius:50%;border:1.5px solid #ccc;display:flex;align-items:center;justify-content:center;color:var(--blue);font-weight:600;font-size:16px}
  .col p{margin-top:24px;font-size:13.3px;line-height:21.6px;color:#555}
  .why{left:132px}
  .what{left:460px}
  .contact{left:787px;width:281px}
  .divider{position:absolute;top:566px;width:1px;height:250px;background:var(--rule)}
  .services{list-style:none;margin-top:22px}
  .services li{font-size:13.3px;line-height:21.6px;color:#555;padding-left:14px;position:relative}
  .services li::before{content:"";position:absolute;left:1px;top:8px;border-left:4px solid var(--blue);border-top:3px solid transparent;border-bottom:3px solid transparent}
  .contact-list{margin-top:22px}
  .contact-item{position:relative;padding-left:27px;margin-bottom:12px;font-size:13.3px;line-height:21.6px;color:#444}
  .contact-item strong{font-weight:600;color:var(--ink)}
  .contact-item svg{position:absolute;left:0;top:4px}

  .site-footer{position:absolute;left:0;top:864px;width:1200px;height:52px;background:var(--footer)}
  .copyright{position:absolute;left:132px;top:18px;font-size:12px;color:#fff}
  .social{position:absolute;right:132px;top:14px;display:flex;gap:5px}
  .social i{width:25px;height:25px;border-radius:50%;background:#fff}
</style>
</head>
<body>
  <header class="site-header">
    <div class="brand"><span class="brand-mark"></span><span class="brand-name">Velric Dunmore, PLLC</span></div>
    <div class="utility">
      <span><svg width="14" height="14" viewBox="0 0 24 24"><path fill="#aaa" d="M6.6 10.8a15 15 0 0 0 6.6 6.6l2.2-2.2c.3-.3.7-.4 1-.2 1.1.4 2.3.6 3.6.6.6 0 1 .4 1 1V20c0 .6-.4 1-1 1A17 17 0 0 1 3 4c0-.6.4-1 1-1h3.5c.6 0 1 .4 1 1 0 1.3.2 2.5.6 3.6.1.3 0 .7-.2 1z"/></svg>(800) 555 014 3306</span>
      <span><svg width="14" height="12" viewBox="0 0 14 12"><path fill="#bbb" d="M0 1l4-1v11l-4 1zM5 0l4 1v11l-4-1zM10 1l4-1v11l-4 1z"/></svg>MAP</span>
    </div>
    <nav class="main-nav">
      <a class="active" href="#">HOME</a><a href="#">FIRM</a><a href="#">PEOPLE</a><a href="#">PRACTICES</a><a href="#">LIBRARY</a><a href="#">NEWS</a>
    </nav>
  </header>

  <section class="hero">
    <div class="hero-photo" role="img" aria-label="Portrait photograph of the attorney outdoors with a blurred green street behind"></div>
    <h1 class="hero-title"><em>COMPANY</em> OVERVIEW</h1>
    <p class="hero-text">I am an Intellectual Property Lawyer and focus on patents, copyrights, trademarks, &amp; trade secrets. I work with small businesses and start ups in the chemical and biotech industries.</p>
    <div class="slider-dots"><i class="on"></i><i></i><i></i><i></i><i></i></div>
  </section>

  <section class="col why">
    <h2>WHY US</h2>
    <span class="col-icon">?</span>
    <p>I am small firm that can provide large-firm service at a reasonable price. I also can charge flat-fees for entrepreneurs in certain practice areas.</p>
  </section>
  <div class="divider" style="left:436px"></div>

  <section class="col what">
    <h2>WHAT WE DO</h2>
    <span class="col-icon"><svg width="18" height="18" viewBox="0 0 24 24"><circle cx="9" cy="14" r="5" fill="none" stroke="#1a6fb0" stroke-width="3" stroke-dasharray="3 2"/><circle cx="17" cy="7" r="3.5" fill="none" stroke="#1a6fb0" stroke-width="2.5" stroke-dasharray="2 1.5"/></svg></span>
    <ul class="services">
      <li>Intellectual Property</li><li>Patents</li><li>Copyrights</li><li>Trademarks</li><li>Trade secrets</li><li>Healthcare Compliance</li><li>Elder law</li><li>Wills</li><li>Trusts</li>
    </ul>
  </section>
  <div class="divider" style="left:764px"></div>

  <section class="col contact">
    <h2>CONTACT INFO</h2>
    <span class="col-icon"><svg width="16" height="18" viewBox="0 0 16 18"><rect x="3" y="1" width="11" height="16" rx="1.5" fill="none" stroke="#1a6fb0" stroke-width="2"/><path d="M1 5h4M1 9h4M1 13h4M7 6h4M7 10h4" stroke="#1a6fb0" stroke-width="1.6"/></svg></span>
    <div class="contact-list">
      <div class="contact-item"><svg width="15" height="14" viewBox="0 0 15 14"><path fill="#ccc" d="M7.5 0L15 7h-2v7H9V9H6v5H2V7H0z"/></svg><strong>Address :</strong><br>262 Lorem Ipsum ,<br>dummy text Contrary to<br>popular belief simply random text</div>
      <div class="contact-item"><svg width="15" height="11" viewBox="0 0 15 11"><rect width="15" height="11" fill="#ccc"/><path d="M0 0l7.5 6L15 0" stroke="#fff" fill="none"/></svg><strong>Email:</strong><br>Contact@velricdunmorepllc.com</div>
      <div class="contact-item"><svg width="14" height="16" viewBox="0 0 24 24"><path fill="#ccc" d="M6.6 10.8a15 15 0 0 0 6.6 6.6l2.2-2.2c.3-.3.7-.4 1-.2 1.1.4 2.3.6 3.6.6.6 0 1 .4 1 1V20c0 .6-.4 1-1 1A17 17 0 0 1 3 4c0-.6.4-1 1-1h3.5c.6 0 1 .4 1 1 0 1.3.2 2.5.6 3.6.1.3 0 .7-.2 1z"/></svg><strong>Phone :</strong><br>(11)11-555-0198</div>
    </div>
  </section>

  <footer class="site-footer">
    <p class="copyright">Copyright © 2014 Velric Dunmore PLLC, All Rights Reserved.</p>
    <div class="social"><i></i><i></i><i></i></div>
  </footer>
</body>
</html>
```